Keratin Clear Clinic - Fungal Nails information booklet

We need an information booklet for a new company that diagnoses and treats fungal nail infections. Once the patient has been diagnosed with a fungal nail infection, we would like to provide them with a booklet (A5 size) that gives them a detailed understanding of what fungal nail infections are, how they get them, what treatment options are available etc. (please find attached the word doc with all of the information we would like included). We have also attached a link to a similar handout that we are after. We have also attached a copy of our logo design and our current letterhead which gives you an idea of the colours that we use. Finally, I have attached some images of before/after pics of our laser treatment, pictures of the laser etc. which we would like used in the laser treatment section of our booklet. The final design should communicate professional, minimalist and clean lined. Please note that we would like the ability to be able to edit the content at a later date if required.

Font styles to use
Serif

Requirements
Must have
• Pictures (feet, fungal nails) - as per handout which can be seen on the document uploaded (Guide_to_TNF_-_ENG_-_TIP_Brochure_-_FINAL_2_Print_Pages)

Before/after pics as per upload in the laser treatment section

```html
<!DOCTYPE html>
<html lang="en">
<head>
<meta charset="utf-8">
<title>Keratin Clear Clinic – Guide to Fungal Nail Infection</title>
<link href="https://fonts.googleapis.com/css2?family=Open+Sans:wght@400;600;700&family=Merriweather:ital,wght@0,300;1,300;1,400&display=swap" rel="stylesheet">
<style>
  :root{
    --backdrop:#444444;
    --paper:#ffffff;
    --brand-blue:#2f5aa8;
    --brand-deep:#1f3f87;
    --heading-blue:#2767b6;
    --heading-navy:#1c2f66;
    --body-ink:#333333;
    --quote-blue:#1f4fa6;
    --blob:#e8eff9;
    --photo-cool:#9fb3de;
    --photo-pale:#dfe6f3;
    --accent-coral:#e06a4e;
  }
  *{box-sizing:border-box;margin:0;padding:0}
  html,body{width:1200px;height:1200px;overflow:hidden;background:var(--backdrop)}
  .spread{position:relative;width:1200px;height:1200px}
  .page{position:absolute;width:378px;height:536px;background:var(--paper);overflow:hidden}
  .page--cover{left:222px;top:43px}
  .page--about{left:638px;top:43px}
  .page--what{left:222px;top:621px}
  .page--effect{left:638px;top:621px}
  .art{position:absolute;left:0;top:0}
  .heading{position:absolute;font-family:"Open Sans",sans-serif;font-weight:400;font-size:21px;line-height:24px;color:var(--heading-blue);text-transform:uppercase;letter-spacing:.3px}
  .heading b{font-weight:600}
  .heading strong{font-weight:700;color:var(--heading-navy)}
  .body-copy{position:absolute;font-family:"Merriweather",serif;font-weight:300;font-size:8.3px;line-height:12.6px;color:var(--body-ink)}
  .body-copy p+p{margin-top:14px}
  .pull-quote{position:absolute;font-family:"Merriweather",serif;font-style:italic;font-size:8.3px;line-height:12.6px;color:var(--quote-blue);text-align:right}
  .quote-rule{position:absolute;width:1px;background:var(--quote-blue)}
  .brand{position:absolute;left:14px;top:20px;width:136px;text-align:center;color:#fff;font-family:"Open Sans",sans-serif;font-weight:600;font-size:10.5px;letter-spacing:1.4px}
  .brand-dot{display:block;width:30px;height:30px;border:2px solid #fff;border-radius:50%;margin:0 auto 8px}
  .cover-title{position:absolute;left:26px;top:366px;font-family:"Open Sans",sans-serif;font-size:24px;line-height:29.2px;color:#fff;text-transform:uppercase}
  .risk-list{list-style:none;margin:10px 0 12px}
  .risk-list li{position:relative;padding-left:16px;margin-bottom:2.6px}
  .risk-list li::before{content:"";position:absolute;left:1px;top:5px;width:2.5px;height:2.5px;border-radius:50%;background:var(--body-ink)}
</style>
</head>
<body>
<main class="spread">

  <!-- Cover -->
  <section class="page page--cover">
    <svg class="art" width="378" height="536" viewBox="0 0 378 536">
      <defs>
        <linearGradient id="coverPhoto" x1="0" y1="0" x2="1" y2="1">
          <stop offset="0" stop-color="var(--photo-pale)"/>
          <stop offset=".55" stop-color="var(--photo-cool)"/>
          <stop offset="1" stop-color="#c8d3ea"/>
        </linearGradient>
        <linearGradient id="coverBlue" x1="0" y1="0" x2="0" y2="1">
          <stop offset="0" stop-color="var(--brand-blue)"/>
          <stop offset="1" stop-color="var(--brand-deep)"/>
        </linearGradient>
      </defs>
      <rect width="378" height="536" fill="url(#coverPhoto)" role="img" aria-label="Photograph of a clinician in gloves examining a patient's toes"/>
      <path d="M0 0H132C150 20 150 70 120 110C70 150 60 200 80 260C100 320 170 340 190 390C210 440 240 500 300 536H0Z" fill="url(#coverBlue)"/>
      <path d="M276 0C268 80 282 150 272 230C262 300 280 380 300 440C318 490 360 510 372 536" fill="none" stroke="#fff" stroke-width="3" stroke-dasharray="1.5 1.5" opacity=".9"/>
      <path d="M318 480C332 472 352 486 360 500C368 516 362 532 352 536H332C322 520 306 492 318 480Z" fill="var(--accent-coral)"/>
    </svg>
    <div class="brand"><span class="brand-dot"></span>KERATIN CLEAR CLINIC</div>
    <h1 class="cover-title">Your<br>complete<br>guide to<br>fungal nail<br>infection</h1>
  </section>

  <!-- About -->
  <section class="page page--about">
    <h2 class="heading" style="left:118px;top:38px">About<br><b>Keratin Clear</b><br><strong>Clinic</strong></h2>
    <div class="body-copy" style="left:118px;top:124px;width:232px">
      <p>At Keratin Clear Clinic, we are your experts at treating fungal nail infections and understand that fungal nail infections can reduce your confidence to wearing open toe shoes and bare feet due to thickened, yellow or irregularly shaped nails. We also understand that getting rid of a fungal nail infection can be extremely difficult involving treatments that are laborious, time consuming and usually unsuccessful.</p>
      <p>Keratin Clear Clinic is a new and innovative clinic specifically looking at the diagnosis and treatment of Fungal nails, bringing the latest technology to the Waikato to treat fungal nail infections. Our clinicians were frustrated by the lack of successful and safe treatments available, therefore, Keratin Clear Clinic have bought our patients the latest in fungal nail treatment which is cold laser therapy. Cold laser therapy provides a simple, safe, and effective up to 87% success rate as well as being a pain free way of treating fungal nail infections.</p>
      <p>Our clinicians here at Keratin Clear Clinic will take the time to diagnose and discuss the right treatment for you. We have comprehensive treatment packages that will be tailored to your needs. These include a combination of laser, topical, oral, and surgical options. Explore our website to discover your fungal nail solution.</p>
    </div>
    <div class="pull-quote" style="left:26px;top:268px;width:75px">“ Cold laser therapy provides a simple, safe, and effective up to 87% success rate as well as being a pain free way of treating fungal nail infections.”</div>
    <div class="quote-rule" style="left:109px;top:268px;height:126px"></div>
    <div class="pull-quote" style="left:26px;top:420px;width:75px">“ We have comprehensive treatment packages that will be tailored to your needs. ”</div>
    <div class="quote-rule" style="left:109px;top:420px;height:76px"></div>
  </section>

  <!-- What is -->
  <section class="page page--what">
    <svg class="art" width="378" height="536" viewBox="0 0 378 536">
      <path d="M210 70C220 30 260 10 300 10C350 10 380 40 378 80V200C360 230 330 240 300 230C270 222 250 210 230 190C205 165 200 110 210 70Z" fill="var(--blob)"/>
      <path d="M0 380C20 360 60 352 90 360C130 370 170 400 176 440C182 490 150 536 120 536H0Z" fill="var(--blob)"/>
      <circle cx="275" cy="105" r="76" fill="#9a9560" role="img" aria-label="Close-up photograph of a yellowed, thickened toenail with fungal infection"/>
      <circle cx="108" cy="440" r="76" fill="#c8a26a" role="img" aria-label="Close-up photograph of a big toe with a yellow, crumbling infected nail"/>
    </svg>
    <h2 class="heading" style="left:32px;top:49px">What is<br><b>a toenail</b><br><b>fungal</b><br><strong>infection?</strong></h2>
    <div class="body-copy" style="left:32px;top:153px;width:156px">
      <p>Onychomycosis also known as a ‘fungal infection’ presents either in the finger or toenails. Fungal nail infections are an extremely common yet treatable nail pathology which makes up about 50% of all nail problems. Unfortunately, fungal infections will not go away on their own without suitable treatment. Early diagnosis and treatment of a fungal infection can certainly increase your chances of a successful cure and helps reduce the change of long-term nail damage.</p>
    </div>
    <div class="body-copy" style="left:194px;top:215px;width:150px">
      <p>Dermatophytes (fungal organisms that require keratin to grow) make up around 90% of all fungal infections. They will most commonly present at the free edge of the nail and slowly spread down the side of the nail towards the nail bed. It is possible for these dermatophytes to spread to the skin causing a fungal skin infection also known as athletes’ foot and athletes’ foot can also cause onychomycosis. Fungal infections prefer to grow in warm, dark, damp environments making toenails far more susceptible to an infection as your shoes and socks make a perfect environment for fungus to grow.</p>
    </div>
  </section>

  <!-- What does it effect -->
  <section class="page page--effect">
    <svg class="art" width="378" height="536" viewBox="0 0 378 536">
      <defs>
        <linearGradient id="footPhoto" x1="0" y1="0" x2="1" y2="1">
          <stop offset="0" stop-color="#c7d9ef"/>
          <stop offset=".5" stop-color="#e7b9ae"/>
          <stop offset="1" stop-color="#d98f87"/>
        </linearGradient>
      </defs>
      <path d="M215 80C225 45 260 30 300 30C345 30 378 50 378 80V260C350 270 320 262 290 250C255 236 225 210 215 170C208 140 208 110 215 80Z" fill="var(--blob)"/>
      <path d="M200 300C215 270 250 255 290 250C330 246 360 240 378 230V536H170C165 480 168 420 180 370C186 345 192 320 200 300Z" fill="url(#footPhoto)" role="img" aria-label="Illustration of an inflamed toe with fungal spores around it"/>
      <circle cx="274" cy="139" r="80" fill="#b8a88a" role="img" aria-label="Close-up photograph of a toenail with pale fungal discolouration"/>
    </svg>
    <h2 class="heading" style="left:33px;top:49px">What does<br><b>toenail</b><br><b>fungus</b><br><strong>effect?</strong></h2>
    <div class="body-copy" style="left:33px;top:153px;width:152px">
      <p>Unfortunately, everybody is at risk of developing a fungal infection, however, there are certain risk factors that put some people at greater risk of infection.</p>
      <ul class="risk-list">
        <li>Age, those 55yrs +</li>
        <li>People who lead active lives as more likely to have sweatier feet.</li>
        <li>Exposure to communal wet areas like swimming pools or showers</li>
        <li>Genetic</li>
        <li>Reduced blood circulation</li>
        <li>Previous or existing injury or infection of the nail or skin</li>
        <li>Weakened immune system (i.e., diabetes)</li>
      </ul>
      <p style="width:150px">Toenail fungus infections are very contagious and are easily passed from one person to another.</p>
    </div>
  </section>

</main>
</body>
</html>
```